Quenda-Ro Flyer (Business Launch)

Using my existing log design for Quenda-Ro Mobile Mechanics, I would like a flyer designed. This would be used for advertising, letterbox drops, handing to the public , door knocking ect.

I'm looking for clean cut simple though with the wow factor, I was thinking of even having the flyer in the shape of a van to promote that I'm a mobile business (I come to you ect)

I've attached copies of my logo and business cards.

I would like the following list of services we provide listed on the flyer (see back of business card).
7 day service (we come to you)
10% discount for online/email booking-enquiry

I think this should be enough for now.

I'm launching this business to aiming to hit the ground running,

Target Market(s)

All motor vehicle owners, house holds, businesses

Industry/Entity Type

Automotive

Font styles to use
Sans Serif
Other font styles liked:
• refer images

Colors
0355a3

Requirements
Must have
• services offered, logo, 7 days, we come to or or catchy phrase to let people know this.
• 10% discount for online/email booking enquiries
• Maintenance Package Servicing from $149 conditions apply
• my preference is for blue, grey and while colour scheme, though also happy to accept artistic design ideas to these.
Nice to have
• Wow factor, brochure that stand out from the rest
• Different share brochure in shape of work van (refer velkaro tramix van)
Should not have
• Not looking for a cheap quick fix, I'm wanting to create a brand .

```html
<!DOCTYPE html>
<html lang="en">
<head>
<meta charset="utf-8">
<title>Quenda-Ro Mobile Mechanics – Flyer</title>
<link href="https://fonts.googleapis.com/css2?family=Open+Sans:wght@300;400;600;700;800&display=swap" rel="stylesheet">
<style>
  :root{
    --brand-blue:#1e8ff2;
    --brand-dark:#2b3034;
    --orange-a:#e0501a;
    --orange-b:#f4892e;
    --ink:#262a2e;
    --panel-top:#2c3034;
    --panel-bottom:#6c747b;
    --band:#5e6b79;
    --band-text:#a9d4ff;
    --white:#ffffff;
    --silver-a:#f4f5f6;
    --silver-b:#9aa0a6;
  }
  *{margin:0;padding:0;box-sizing:border-box}
  html,body{width:1200px;height:2545px;overflow:hidden;background:var(--white)}
  body{font-family:"Open Sans",Arial,sans-serif;color:var(--ink)}
  .flyer{position:relative;width:1200px;height:2545px;overflow:hidden;background:var(--white)}

  .brand{position:absolute;left:102px;top:110px;display:flex;align-items:center;gap:44px}
  .brand-mark{width:220px;height:220px;border-radius:50%;background:var(--brand-blue)}
  .brand-name{font-weight:800;font-size:96px;line-height:1.02;color:var(--brand-dark);letter-spacing:-1px}

  .headline{position:absolute;left:0;width:1200px;text-align:center}
  .headline-main{top:405px;font-weight:700;font-size:158px;line-height:1;
    background:linear-gradient(90deg,var(--orange-a),var(--orange-b));
    -webkit-background-clip:text;background-clip:text;color:transparent}
  .headline-sub{top:568px;font-weight:300;font-size:128px;line-height:1;
    background:linear-gradient(90deg,var(--orange-a),var(--orange-b));
    -webkit-background-clip:text;background-clip:text;color:transparent}

  .photo{position:absolute;left:0;top:790px;width:1200px;height:935px;
    background:
      linear-gradient(180deg,#ffffff 0%,rgba(255,255,255,0) 28%),
      linear-gradient(90deg,#9aa3ab 0%,#c9cdd0 35%,#4a5560 60%,#8f9aa4 100%)}

  .offer{position:absolute;right:96px;top:766px;text-align:center;width:474px}
  .offer-badge{display:block;height:80px;border-radius:8px;
    background:linear-gradient(180deg,#4aa6ff,#1679e0);
    color:var(--white);font-weight:700;font-size:46px;line-height:80px}
  .offer-text{margin-top:12px;font-weight:700;font-size:45px;line-height:70px;color:var(--ink)}

  .services{position:absolute;left:0;top:1720px;width:1200px;height:567px;
    background:linear-gradient(180deg,var(--panel-top),var(--panel-bottom))}
  .services-tab{position:absolute;left:0;top:0;width:1200px;height:120px}
  .services-title{position:absolute;left:0;top:20px;width:1200px;text-align:center;
    color:var(--white);font-weight:700;font-size:58px;text-shadow:0 3px 6px rgba(0,0,0,.55)}
  .service-list{position:absolute;left:190px;top:150px;list-style:none}
  .service-list li{display:flex;align-items:center;gap:26px;height:76px;
    font-size:50px;color:var(--white);font-weight:400}
  .service-list li::before{content:"";width:30px;height:30px;border-radius:50%;background:var(--white);flex:none}

  .promo{position:absolute;left:0;top:2287px;width:1200px;height:258px;background:var(--band);text-align:center}
  .promo-price{position:absolute;left:0;top:42px;width:1200px;font-weight:600;font-size:44px;color:var(--band-text)}
  .promo-terms{position:absolute;right:145px;top:100px;font-size:13px;color:#dfe6ee}
  .contact{position:absolute;left:0;top:170px;width:1200px;font-size:32px;letter-spacing:9px;color:var(--white)}
</style>
</head>
<body>
<main class="flyer">
  <header class="brand">
    <span class="brand-mark"></span>
    <span class="brand-name">Quenda-Ro<br>Mobile Mechanics</span>
  </header>

  <h1 class="headline headline-main">7 DAY SERVICE</h1>
  <p class="headline headline-sub">(WE COME TO YOU)</p>

  <div class="photo" role="img" aria-label="Photo of a smiling customer on the phone while a mechanic in overalls works under the raised bonnet of a silver car"></div>

  <aside class="offer">
    <span class="offer-badge">10% DISCOUNT</span>
    <p class="offer-text">FOR ONLINE/EMAIL<br>BOOKING-ENQUIRY</p>
  </aside>

  <section class="services">
    <svg class="services-tab" viewBox="0 0 1200 120" preserveAspectRatio="none" aria-hidden="true">
      <defs>
        <linearGradient id="tabFill" x1="0" y1="0" x2="0" y2="1">
          <stop offset="0" stop-color="#f4f5f6"/>
          <stop offset="1" stop-color="#8d949a"/>
        </linearGradient>
      </defs>
      <path d="M0 0 H1200 V6 H980 Q950 6 935 40 L920 80 Q905 112 870 112 H330 Q295 112 280 80 L265 40 Q250 6 220 6 H0 Z" fill="url(#tabFill)"/>
    </svg>
    <h2 class="services-title">SERVICES OFFERED</h2>
    <ul class="service-list">
      <li>Servicing and Repairs</li>
      <li>Manufacturers Log Book Service</li>
      <li>Mantenance Package Service</li>
      <li>Pre-Purchase Inspections</li>
    </ul>
  </section>

  <footer class="promo">
    <p class="promo-price">Maintenance Package Servicing from $149</p>
    <p class="promo-terms">conditions apply*</p>
    <p class="contact">Contact detail goes here</p>
  </footer>
</main>
</body>
</html>
```